New Corporate website more focused on funnel and great design

Our company, Bold Harbor needs a new website to look like it's from 2021. We work with large businesses in the corporte world and need to reflect that we are professional, focused on our clients, and trsutworthy. It should include some/most of the components from our current site: boldharbor.com but should focus more about getting people to optin to out free downloads, which can be found on this page: https://www.boldharbor.com/get-started-with-a-prep-session/ and this page: https://www.boldharbor.com/team-onboarding/

Our new website should do a better job at explaining what we do, who we serve, and how we fix their problems of onboarding new leaders. Feel free to use dummy text if you are not sure what to put in for certain sections. I also would like to point out that most of the audiance is older, so we don't need anything too younge and flashy, or that is hard it use. it should have big clear fonts, plently of contrast, and work well for poeple who are not good at using the internet. Please use the colors of the logo, and you can add another color or two if you think it's fits

Industry/Entity Type

business consulting

Number of Pages Required

2 page

Font styles to use
Sans Serif

Requirements
Must have
• corporate feel, look professional, focus on getting new leads
Should not have
• cute or children feel

```html
<!DOCTYPE html>
<html lang="en">
<head>
<meta charset="utf-8">
<title>Bold Harbor | Better Results Faster</title>
<link rel="stylesheet" href="https://fonts.googleapis.com/css2?family=Roboto:wght@300;400;500;700;900&display=swap">
<style>
  :root {
    --brand-blue: #2a7af6;
    --ink: #222222;
    --body-text: #333333;
    --white: #ffffff;
    --placeholder: #c4c4c4;
    --card-border: #e2e2e2;
    --footer-bg: #000000;
    --hero-dark: #2b3340;
    --hero-mid: #4a5566;
    --hero-light: #7d8796;
  }
  * { box-sizing: border-box; margin: 0; padding: 0; }
  html, body { width: 1200px; height: 3812px; overflow: hidden; }
  body {
    position: relative;
    background: var(--white);
    font-family: "Roboto", Arial, sans-serif;
    color: var(--ink);
  }
  .abs { position: absolute; }

  /* Buttons */
  .btn {
    position: absolute;
    display: flex; align-items: center; justify-content: center;
    border-radius: 20px;
    font-size: 14px; font-weight: 700; letter-spacing: 1.6px;
    text-transform: uppercase; text-decoration: none;
  }
  .btn--solid { background: var(--brand-blue); color: var(--white); }
  .btn--outline { border: 1.5px solid var(--brand-blue); color: var(--ink); background: var(--white); }
  .btn--outline-light { border: 1.5px solid var(--white); color: var(--white); background: transparent; }

  /* Hero */
  .hero { position: absolute; left: 0; top: 0; width: 1200px; height: 553px; overflow: hidden; }
  .hero__photo {
    position: absolute; inset: 0;
    background:
      radial-gradient(ellipse 420px 360px at 830px 230px, var(--hero-light), transparent 70%),
      radial-gradient(ellipse 300px 400px at 120px 320px, #3a3f48, transparent 70%),
      linear-gradient(100deg, var(--hero-dark) 0%, var(--hero-mid) 45%, #5e6a7a 70%, var(--hero-dark) 100%);
  }
  .hero__shade { position: absolute; inset: 0; background: rgba(30, 40, 60, 0.35); }
  .brand {
    position: absolute; display: flex; align-items: center; gap: 10px;
    font-weight: 500; text-decoration: none;
  }
  .brand__mark { width: 22px; height: 22px; background: var(--brand-blue); }
  .brand--header { left: 52px; top: 42px; font-size: 22px; color: var(--brand-blue); }
  .nav { position: absolute; top: 51px; left: 0; width: 1200px; height: 16px; }
  .nav a {
    position: absolute; top: 0; color: var(--white); text-decoration: none;
    font-size: 12.5px; font-weight: 700; letter-spacing: 1px;
  }
  .hero__title {
    position: absolute; top: 150px; left: 0; width: 1200px; text-align: center;
    font-size: 98px; font-weight: 700; color: var(--white); letter-spacing: 1px; line-height: 1.1;
  }
  .hero__subtitle {
    position: absolute; top: 285px; left: 0; width: 1200px; text-align: center;
    font-size: 20px; font-weight: 500; color: var(--white); letter-spacing: 3px;
  }

  /* Section headings */
  .section-title { position: absolute; font-size: 51px; font-weight: 700; letter-spacing: 2px; color: var(--ink); line-height: 1; }
  .section-lead {
    position: absolute; left: 89px; width: 960px;
    font-size: 22px; line-height: 30px; letter-spacing: 3.2px; color: var(--ink);
  }

  /* About */
  .about__facts {
    position: absolute; left: 89px; top: 740px; width: 460px;
    font-size: 30px; font-weight: 300; line-height: 51px; letter-spacing: 1px; color: var(--body-text);
  }
  .about__copy { position: absolute; left: 622px; top: 741px; width: 495px; }
  .about__copy p { font-size: 15.5px; line-height: 22.3px; color: var(--body-text); margin-bottom: 22px; }

  /* Work grid */
  .work-tile { position: absolute; width: 330px; height: 329px; background: var(--placeholder); }

  /* Service cards */
  .service-card {
    position: absolute; top: 2439px; width: 330px; height: 329px;
    background: var(--white); border: 1px solid var(--card-border);
    box-shadow: 0 1px 4px rgba(0,0,0,0.12);
    padding: 24px 20px 0 21px;
  }
  .service-card__title { font-size: 25.5px; font-weight: 500; color: var(--ink); line-height: 1.2; }
  .service-card__stat { margin-top: 12px; font-size: 17px; color: var(--brand-blue); letter-spacing: 0.4px; }
  .service-card__body { margin-top: 18px; font-size: 16.5px; line-height: 26px; color: var(--body-text); letter-spacing: 0.3px; }

  /* CTA band */
  .cta { position: absolute; left: 0; top: 3029px; width: 1200px; height: 667px; background: var(--brand-blue); }
  .brand--cta { left: 415px; top: 3213px; font-size: 34px; color: var(--hero-dark); }
  .brand--cta .brand__mark { width: 34px; height: 34px; background: var(--hero-dark); }
  .cta__title {
    position: absolute; left: 0; top: 3305px; width: 1146px; text-align: center;
    font-size: 75px; font-weight: 700; color: var(--white); line-height: 1.2;
  }

  /* Footer */
  .site-footer { position: absolute; left: 0; top: 3696px; width: 1200px; height: 116px; background: var(--footer-bg); }
  .site-footer__text {
    position: absolute; top: 52px; left: 0; width: 1200px; text-align: center;
    font-size: 13.5px; font-weight: 700; letter-spacing: 3px; color: var(--white);
  }
</style>
</head>
<body>

<header class="hero">
  <div class="hero__photo" role="img" aria-label="Photo of a business leader in conversation with colleagues across a table"></div>
  <div class="hero__shade"></div>
  <a class="brand brand--header" href="#"><span class="brand__mark"></span>Bold Harbor</a>
  <nav class="nav">
    <a href="#" style="left:530px">Who We Are</a>
    <a href="#" style="left:641px">What We Do</a>
    <a href="#" style="left:750px">Clients</a>
    <a href="#" style="left:827px">Blog</a>
    <a href="#" style="left:888px">Resources</a>
  </nav>
  <a class="btn btn--solid" href="#" style="left:991px;top:37px;width:152px;height:38px;">Contact Us</a>
  <h1 class="hero__title">Accelerate</h1>
  <p class="hero__subtitle">BUSINESS PERFORMANCE DURING CRITICAL LEADERSHIP TRANSITIONS</p>
  <a class="btn btn--solid" href="#" style="left:506px;top:361px;width:187px;height:37px;">View Our Work</a>
</header>

<section class="about">
  <h2 class="section-title" style="left:624px;top:636px;">About Us</h2>
  <p class="about__facts">Get done in 100 days what normally takes 6-12 months 90% of Bold Harbor clients succeed</p>
  <div class="about__copy">
    <p>Lorem ipsum dolor sit amet, consectetur adipiscing elit. Sed et justo ac lectus blandit ullamcorper sit amet et erat. Vivamus vitae</p>
    <p>Lorem ipsum dolor sit amet, consectetur adipiscing elit. Sed et justo ac lectus blandit ullamcorper sit amet et erat. Vivamus vitae</p>
    <p>Lorem ipsum dolor sit amet, consectetur adipiscing elit. Sed et justo ac lectus blandit ullamcorper sit amet et erat. Vivamus vitae dui sit amet quam vestibulum lobortis quis a sem. Aenean tristique ut arcu at gravida. Suspendisse potenti. Morbi nec nisi ut dolor faucibus porttitor eu eget odio. Nunc hendrerit lectus a diam venenatis, mattis placerat elit rhoncus. Orci varius natoque penatibus et magnis dis parturient montes, nascetur ridiculus mus. Mauris blandit est est, in placerat justo mattis non. Proin commodo, dui et congue dapibus, mi ligula auctor urna, nec fringilla mauris mauris et felis. Nam auctor malesuada nulla, eu pellentesque metus.</p>
  </div>
  <a class="btn btn--outline" href="#" style="left:623px;top:1138px;width:158px;height:36px;">Learn More</a>
</section>

<section class="work">
  <h2 class="section-title" style="left:78px;top:1253px;">Our Work</h2>
  <p class="section-lead" style="top:1315px;">Lorem ipsum dolor sit amet, consectetur adipiscing elit. Sed et justo ac lectus blandit ullamcorper sit amet et erat. Vivamus vitae</p>
  <div class="work-tile" style="left:78px;top:1465px;"></div>
  <div class="work-tile" style="left:435px;top:1465px;"></div>
  <div class="work-tile" style="left:792px;top:1465px;"></div>
  <div class="work-tile" style="left:78px;top:1811px;"></div>
  <div class="work-tile" style="left:435px;top:1811px;"></div>
  <div class="work-tile" style="left:792px;top:1811px;"></div>
</section>

<section class="services">
  <h2 class="section-title" style="left:78px;top:2264px;">What We Do</h2>
  <p class="section-lead" style="top:2317px;">Lorem ipsum dolor sit amet, consectetur adipiscing elit. Sed et justo ac lectus blandit ullamcorper sit amet et erat. Vivamus vitae</p>

  <article class="service-card" style="left:78px;">
    <h3 class="service-card__title">Executive Onboarding</h3>
    <p class="service-card__stat">40% of new leaders fail</p>
    <p class="service-card__body">For executive leaders taking on new roles, the Bold Harbor 100-Day Action Plan process prepares leaders before the start, speeds up assimilation, sets direction, builds the team, accelerates momentum, and delivers results.</p>
  </article>
  <article class="service-card" style="left:435px;">
    <h3 class="service-card__title">Team Onboarding</h3>
    <p class="service-card__stat">80% of M&amp;A fail to boost returns</p>
    <p class="service-card__body">For leaders integrating teams post acquisition or re-organization, the Bold Harbor 100 Day Action Plan process gets all players on board with the change and accelerates achievement of cultural and business integration goals.</p>
  </article>
  <article class="service-card" style="left:792px;">
    <h3 class="service-card__title">Acceleration &amp; Restart</h3>
    <p class="service-card__stat">70% of transformations fall short</p>
    <p class="service-card__body">For executives leading through a strategic point of inflection or reinvigorating a stalled team, Bold Harbor programs define the from-to challenge, kickstart a change process and deliver results that stick.</p>
  </article>

  <a class="btn btn--solid" href="#" style="left:506px;top:2863px;width:187px;height:37px;">View Our Work</a>
</section>

<section class="cta"></section>
<a class="brand brand--cta" href="#"><span class="brand__mark"></span>Bold Harbor</a>
<h2 class="cta__title">Ready to Talk?</h2>
<a class="btn btn--outline-light" href="#" style="left:479px;top:3470px;width:188px;height:36px;">View Our Work</a>

<footer class="site-footer">
  <p class="site-footer__text">2021 Bold Harbor | BETTER RESULTS FASTER</p>
</footer>

</body>
</html>
```